Harlow Vance Law Stationary - logo provided

I need Stationary designed for my Law Firm named Harlow Vance Law.

I have attached the firm's logo and would like that color and logos incorporated into the stationary. I need the stationary to look clean, simple and professional.

I need letterheads, envelopes and business cards designed. I would also like a letterhead version for 5.5 x 8..5 paper size (for handout printing)

Industry/Entity Type

Legal

```html
<!DOCTYPE html>
<html lang="en">
<head>
<meta charset="UTF-8">
<title>Harlow Vance Law – Letterhead</title>
<link rel="stylesheet" href="https://fonts.googleapis.com/css2?family=Cinzel:wght@600&display=swap">
<style>
  :root {
    --paper: #fbf9f4;
    --paper-shade: #efe9dc;
    --maroon: #7b1f22;
    --gold: #b89b6a;
    --gold-light: #d2bb92;
    --border: #9a9a9a;
  }
  html, body {
    margin: 0;
    padding: 0;
    width: 849px;
    height: 1200px;
    overflow: hidden;
    background: #ffffff;
  }
  .letterhead {
    position: relative;
    width: 849px;
    height: 1200px;
    box-sizing: border-box;
    border: 2px solid var(--border);
    background: radial-gradient(ellipse at 50% 45%, var(--paper) 40%, var(--paper-shade) 100%);
    overflow: hidden;
  }
  .corner-fold {
    position: absolute;
    left: 0;
    top: 0;
    width: 320px;
    height: 320px;
  }
  .brand {
    position: absolute;
    top: 36px;
    right: 44px;
    display: flex;
    align-items: center;
    gap: 18px;
  }
  .brand-square {
    width: 64px;
    height: 64px;
    border: 4px solid var(--maroon);
    box-sizing: border-box;
  }
  .brand-name {
    font-family: "Cinzel", "Times New Roman", serif;
    font-weight: 600;
    font-size: 40px;
    line-height: 1.05;
    letter-spacing: 2px;
    color: var(--maroon);
    margin: 0;
  }
  .footer-band {
    position: absolute;
    left: 0;
    bottom: 0;
    width: 849px;
    height: 110px;
  }
  .footer-mark {
    position: absolute;
    left: 50%;
    bottom: 22px;
    width: 30px;
    height: 30px;
    margin-left: -15px;
    background: var(--maroon);
  }
</style>
</head>
<body>
  <main class="letterhead">
    <svg class="corner-fold" viewBox="0 0 320 320" aria-hidden="true">
      <polygon points="0,0 268,0 214,58 120,150 40,290 0,290" fill="var(--gold)"/>
      <polyline points="268,0 214,58 120,150 40,290" fill="none" stroke="var(--maroon)" stroke-width="6"/>
      <polygon points="214,58 268,0 250,64" fill="var(--gold-light)"/>
      <circle cx="192" cy="132" r="38" fill="var(--paper)" stroke="var(--gold-light)" stroke-width="4"/>
      <circle cx="192" cy="132" r="26" fill="var(--gold-light)"/>
    </svg>

    <header class="brand">
      <div class="brand-square"></div>
      <h1 class="brand-name">Harlow Vance<br>Law</h1>
    </header>

    <svg class="footer-band" viewBox="0 0 849 110" preserveAspectRatio="none" aria-hidden="true">
      <path d="M0,110 L0,78 Q424,-8 849,78 L849,110 Z" fill="var(--gold)"/>
      <path d="M0,66 Q424,-22 849,66" fill="none" stroke="var(--maroon)" stroke-width="3"/>
    </svg>
    <div class="footer-mark"></div>
  </main>
</body>
</html>
```